Law Firm Stationery Design - Traditional Meets Intuitive

Looking for a modern, yet classic, law firm stationery design. Simplicity is desired, but great ideas are encouraged. See attachment for company information. We utilize a variety of non-traditional legal tools to bring a different perspective to each of our client's particular situation. Final design should communicate classic values with intuitive, unique solutions.

Industry/Entity Type

Law Firm

Requirements
Should not have
• - No typical legal icons
• - No Tag Line!
• - DO NOT WANT WHAT WE ALREADY HAVE

```html
<!DOCTYPE html>
<html lang="en">
<head>
<meta charset="UTF-8">
<title>Veridane Law – Business Card</title>
<link rel="stylesheet" href="https://fonts.googleapis.com/css2?family=Old+Standard+TT:wght@400;700&family=Arimo:wght@400;700&display=swap">
<style>
  :root {
    --page-bg: #e6e4e0;
    --card-black: #0c0c0c;
    --card-black-edge: #262626;
    --ink: #1a1a1a;
    --ink-soft: #4a4a4a;
    --ink-light: #e4e4e4;
    --ink-muted: #9a9a9a;
    --accent-blue: #1d6fb3;
    --serif: "Old Standard TT", "Times New Roman", serif;
    --sans: "Arimo", Arial, sans-serif;
  }
  * { box-sizing: border-box; margin: 0; padding: 0; }
  html, body {
    width: 1200px; height: 950px; overflow: hidden;
    background: var(--page-bg);
  }
  .canvas {
    position: relative; width: 1200px; height: 950px;
    display: flex; flex-direction: column; align-items: center;
    justify-content: center; gap: 50px;
  }
  .card {
    position: relative; width: 700px; height: 400px;
    box-shadow: 0 8px 24px rgba(0,0,0,.18);
  }

  /* Back of card */
  .card-back {
    background: linear-gradient(120deg, var(--card-black) 0%, var(--card-black) 62%, var(--card-black-edge) 78%, var(--card-black) 92%);
    text-align: center;
  }
  .card-back .brand-name {
    position: absolute; left: 0; right: 0; top: 140px;
    font-family: var(--serif); font-weight: 400;
    font-size: 68px; line-height: 1; letter-spacing: 1px;
    color: var(--ink-light);
  }
  .card-back .brand-web {
    position: absolute; left: 0; right: 0; bottom: 70px;
    font-family: var(--sans); font-size: 15px;
    letter-spacing: 7px; color: var(--ink-muted);
  }

  /* Front of card */
  .card-front {
    background: linear-gradient(160deg, #ffffff 0%, #fafafa 60%, #ececec 100%);
    color: var(--ink);
  }
  .accent-bar {
    position: absolute; left: 0; top: 92px;
    width: 18px; height: 46px; background: var(--accent-blue);
  }
  .person {
    position: absolute; left: 40px; top: 98px;
  }
  .person-name {
    font-family: var(--sans); font-weight: 700;
    font-size: 19px; letter-spacing: .5px; color: #111;
  }
  .person-title {
    font-family: var(--sans); font-size: 17px;
    color: var(--accent-blue); margin-top: 2px;
  }
  .front-brand {
    position: absolute; right: 50px; top: 80px;
    font-family: var(--serif); font-weight: 400;
    font-size: 52px; line-height: 1; color: #111;
  }
  .contact {
    position: absolute; right: 50px; bottom: 36px; text-align: right;
    font-family: var(--sans); font-style: normal; font-size: 17px; line-height: 1.45;
    color: var(--ink-soft);
  }
  .contact .label { font-weight: 700; color: #222; }
</style>
</head>
<body>
<main class="canvas">
  <section class="card card-back">
    <div class="brand-name">Veridane Law</div>
    <div class="brand-web">www.veridanelaw.com</div>
  </section>

  <section class="card card-front">
    <div class="accent-bar"></div>
    <div class="person">
      <div class="person-name">MARK ELLISON</div>
      <div class="person-title">President</div>
    </div>
    <div class="front-brand">Veridane Law</div>
    <address class="contact">
      <div>VERIDANE LAW LLC</div>
      <div>18 Harbor Lane, Suite 300, Westfield, MA 01085</div>
      <div><span class="label">P:</span> 555-014-2200 &nbsp;<span class="label">E:</span> info@veridanelaw.com</div>
      <div><span class="label">W:</span> www.veridanelaw.com</div>
    </address>
  </section>
</main>
</body>
</html>
```